Lumen Kinetics Web Design Project

We need to update our web design for our company. Lumen Kinetics™ is a series of Development (Training) Programs that we deliver both for the General Public as well as Corporate Business.

Much of the content needs a refresh but we are keen to get some thoughts now on design and layout, predominantly front page. Happy to take any comments on the content if you think that is relevant as well.

We might look to move the current video clip and bring a more generic 'inspirational' clip to the front page. A good example of this is www.mindcraftoz.example.au

Our courses have a very similar market to Gerald Whitcombe type courses ... both General Public and Corporate business.

Refer our website www.lumenkinetics.example.com

Target Market(s)

General Public as well as Corporate Business. Courses are designed for all. Gerald Whitcombe would be a good 'feel' for what we do.

Industry/Entity Type

Business

Requirements
Must have
• Must have a 'leading edge' type feel to it.
Must look professional.

```html
<!DOCTYPE html>
<html lang="en">
<head>
<meta charset="utf-8">
<title>Lumen Kinetics</title>
<link href="https://fonts.googleapis.com/css2?family=Arimo:wght@400;700&display=swap" rel="stylesheet">
<style>
  :root {
    --bar-dark: #212121;
    --white: #ffffff;
    --brand-blue: #1b6fb5;
    --headline-blue: #4c9fd6;
    --nav-text: #444444;
    --body-grey: #7a7a7a;
    --copy-grey: #555555;
    --dot-grey: #9a9a9a;
    --dot-active: #4c9fd6;
    --stripe-blue: #46a8dc;
    --stripe-yellow: #f3e205;
    --stripe-pink: #e0166c;
    --frame-light: #e4e4e4;
    --frame-mid: #c2c2c2;
  }
  * { margin: 0; padding: 0; box-sizing: border-box; }
  html, body { width: 1200px; height: 1005px; overflow: hidden; }
  body { font-family: "Arimo", Arial, sans-serif; background: var(--white); position: relative; }

  .top-bar { position: absolute; left: 0; top: 0; width: 1200px; height: 85px; background: var(--bar-dark); color: var(--white); }
  .account-links { position: absolute; left: 109px; top: 38px; font-size: 17px; display: flex; align-items: center; }
  .account-links .divider { width: 1px; height: 20px; background: var(--white); margin: 0 15px 0 17px; }
  .newsletter { position: absolute; left: 637px; top: 38px; font-size: 17px; display: flex; align-items: center; gap: 14px; }
  .phone { position: absolute; left: 896px; top: 32px; font-size: 23px; font-weight: 700; display: flex; align-items: center; gap: 12px; }
  .top-tab { position: absolute; left: 485px; top: 85px; width: 68px; height: 9px; background: var(--bar-dark); }

  .brand { position: absolute; left: 114px; top: 112px; color: var(--brand-blue); font-size: 36px; line-height: 36px; font-weight: 400; letter-spacing: 0.5px; }

  .main-nav { position: absolute; right: 92px; top: 164px; display: flex; align-items: center; color: var(--nav-text); font-size: 17px; }
  .main-nav .sep { margin: 0 14px; font-size: 13px; }
  .main-nav .small { font-size: 15px; }
  .main-nav sup { font-size: 9px; }

  .hero { position: absolute; left: 0; top: 230px; width: 1200px; height: 571px;
    background: radial-gradient(ellipse 70% 60% at 50% 45%, #ffffff 55%, #ececec 100%); }
  .hero-title { position: absolute; left: 115px; top: 117px; width: 320px; color: var(--headline-blue); font-size: 36px; line-height: 40.5px; font-weight: 400; }
  .hero-sub { position: absolute; left: 110px; top: 344px; width: 280px; color: var(--body-grey); font-size: 19px; line-height: 31px; }
  .slider-dots { position: absolute; left: 110px; top: 509px; display: flex; gap: 11px; }
  .slider-dots span { width: 10px; height: 10px; border-radius: 50%; background: var(--dot-grey); }
  .slider-dots span.active { background: var(--dot-active); }

  .monitor { position: absolute; left: 522px; top: 72px; }
  .stripe { position: absolute; left: 170px; top: 564px; display: flex; height: 7px; }
  .stripe span { width: 287px; height: 7px; }

  .intro { position: absolute; left: 0; top: 850px; width: 1200px; text-align: center; color: var(--copy-grey); font-size: 32px; line-height: 38px; }
</style>
</head>
<body>
  <header class="top-bar">
    <div class="account-links"><span>Log In</span><span class="divider"></span><span>Register</span></div>
    <div class="newsletter">
      <svg width="27" height="18" viewBox="0 0 27 18" aria-hidden="true"><rect x="0" y="0" width="27" height="18" fill="#fff"/><path d="M0 0 L13.5 10 L27 0" fill="none" stroke="#212121" stroke-width="2"/><path d="M0 18 L10 8 M27 18 L17 8" stroke="#212121" stroke-width="1.5"/></svg>
      <span>Sign up to our newsletter</span>
    </div>
    <div class="phone">
      <svg width="28" height="30" viewBox="0 0 28 30" aria-hidden="true"><rect x="0" y="1" width="8" height="28" rx="2" fill="#fff"/><rect x="10" y="3" width="18" height="25" rx="2" fill="#fff"/><g fill="#212121"><rect x="13" y="6" width="12" height="4"/><rect x="13" y="13" width="3" height="3"/><rect x="18" y="13" width="3" height="3"/><rect x="23" y="13" width="2" height="3"/><rect x="13" y="18" width="3" height="3"/><rect x="18" y="18" width="3" height="3"/><rect x="23" y="18" width="2" height="3"/><rect x="13" y="23" width="3" height="3"/><rect x="18" y="23" width="3" height="3"/></g></svg>
      <span>+61 390 555 018</span>
    </div>
  </header>
  <div class="top-tab"></div>

  <div class="brand">Lumen<br>Kinetics</div>

  <nav class="main-nav">
    <span class="small">Home</span><span class="sep">I</span>
    <span>Lumen Kinetics<sup>TM</sup></span><span class="sep">I</span>
    <span>About Us</span><span class="sep">I</span>
    <span>Articles and Resource</span><span class="sep">I</span>
    <span class="small">Contact Us</span>
  </nav>

  <section class="hero">
    <h1 class="hero-title">Consequuntur dolores explicabo nemo voluptem aut natus?</h1>
    <p class="hero-sub">Aspernatur magni quae aut veritatis beatae eos aut voluptas</p>
    <div class="slider-dots"><span></span><span></span><span></span><span class="active"></span><span></span></div>

    <svg class="monitor" width="578" height="450" viewBox="0 0 578 450">
      <defs>
        <linearGradient id="frameGrad" x1="0" y1="0" x2="0" y2="1"><stop offset="0" stop-color="#eeeeee"/><stop offset="1" stop-color="#c8c8c8"/></linearGradient>
        <linearGradient id="standGrad" x1="0" y1="0" x2="1" y2="0"><stop offset="0" stop-color="#b9b9b9"/><stop offset="0.5" stop-color="#eeeeee"/><stop offset="1" stop-color="#b0b0b0"/></linearGradient>
        <linearGradient id="screenGrad" x1="0" y1="0" x2="1" y2="1"><stop offset="0" stop-color="#e9ecef"/><stop offset="0.45" stop-color="#b9c4cf"/><stop offset="1" stop-color="#8c8f99"/></linearGradient>
        <radialGradient id="shadowGrad"><stop offset="0" stop-color="#9a9a9a"/><stop offset="1" stop-color="#9a9a9a" stop-opacity="0"/></radialGradient>
      </defs>
      <ellipse cx="290" cy="430" rx="230" ry="22" fill="url(#shadowGrad)"/>
      <path d="M215 376 L363 376 L370 440 L208 440 Z" fill="url(#standGrad)"/>
      <rect x="193" y="440" width="190" height="7" rx="2" fill="#a8a8a8"/>
      <rect x="0" y="0" width="577" height="376" fill="url(#frameGrad)" stroke="#bdbdbd"/>
      <rect x="16" y="17" width="545" height="338" fill="url(#screenGrad)" role="img" aria-label="Video still: colleagues smiling around a meeting table"/>
      <rect x="243" y="154" width="90" height="62" rx="12" fill="#4a4a4a" opacity="0.85"/>
      <path d="M276 170 L276 200 L302 185 Z" fill="#fff"/>
    </svg>

    <div class="stripe"><span style="background:var(--stripe-blue)"></span><span style="background:var(--stripe-yellow)"></span><span style="background:var(--stripe-pink)"></span></div>
  </section>

  <p class="intro">amet eaque eaque totam ratione voluptas error<br>eaque iste perspiciatis voluptas laudantium voluptatem<br>consequuntur dolores explicabo</p>
</body>
</html>
```